Social Media Graphics - Harbor Climb REVISED

Create 6-7 individual social media graphics (square size) to encourage folks to join our online course called:

The Lantern Ledger Plan
How to Launch a Multi-Million Business From Scratch
Sign Up Today!

IMPORTANT: Make the largest and most prominent text on the graphic be: How to Launch a Multi-Million Business From Scratch

For the color scheme of the graphics, let's try a blue color palette; make sure the graphics appeal to both men and women

Make sure each graphic contains 1 of the 3 pics attached (crop pic as needed); and make sure one of the graphics is all TEXT only.

Target Market(s)

men and women looking to start a business

Industry/Entity Type

Entrepreneurship

Colors
0054AA
0677BA
7BADD7
CADEEF
E8F1F8

Requirements
Must have
• All the text and use the 3 pics provided; one graphic can be all text; Simple, modern design that's easy to read

```html
<!DOCTYPE html>
<html lang="en">
<head>
<meta charset="UTF-8">
<title>The Lantern Ledger Plan – Social Graphic</title>
<link href="https://fonts.googleapis.com/css2?family=League+Spartan:wght@700&family=Montserrat:wght@700;800&display=swap" rel="stylesheet">
<style>
  :root {
    --brand-blue: #0054AA;
    --mid-blue: #0677BA;
    --soft-blue: #7BADD7;
    --pale-blue: #CADEEF;
    --mist-blue: #E8F1F8;
    --white: #FFFFFF;
    --photo-dark: #1E2A44;
    --photo-denim: #2F5E8E;
  }
  html, body {
    margin: 0;
    padding: 0;
    width: 1200px;
    height: 1200px;
    overflow: hidden;
    background: var(--brand-blue);
  }
  .graphic {
    position: relative;
    width: 1200px;
    height: 1200px;
    overflow: hidden;
    background: var(--brand-blue);
  }
  .backdrop {
    position: absolute;
    inset: 0;
    width: 1200px;
    height: 1200px;
  }
  .headline {
    position: absolute;
    left: 78px;
    top: 89px;
    margin: 0;
    font-family: "League Spartan", "Montserrat", sans-serif;
    font-weight: 700;
    font-size: 124px;
    line-height: 113px;
    letter-spacing: 1px;
    color: var(--white);
    text-transform: uppercase;
    white-space: nowrap;
  }
  .course-name {
    position: absolute;
    left: 78px;
    top: 603px;
    margin: 0;
    font-family: "Montserrat", sans-serif;
    font-weight: 700;
    font-size: 37px;
    letter-spacing: 1.5px;
    color: var(--white);
    white-space: nowrap;
  }
  .cta-button {
    position: absolute;
    left: 77px;
    top: 720px;
    width: 342px;
    height: 77px;
    border-radius: 7px;
    background: var(--pale-blue);
    color: var(--brand-blue);
    font-family: "Montserrat", sans-serif;
    font-weight: 700;
    font-size: 27px;
    display: flex;
    align-items: center;
    justify-content: center;
    text-decoration: none;
  }
  .hosts-photo {
    position: absolute;
    left: 450px;
    top: 680px;
    width: 750px;
    height: 520px;
    border-top-left-radius: 40px;
    background: linear-gradient(100deg, var(--photo-dark) 0%, #243655 55%, var(--photo-denim) 100%);
  }
</style>
</head>
<body>
  <main class="graphic">
    <svg class="backdrop" viewBox="0 0 1200 1200" aria-hidden="true">
      <defs>
        <linearGradient id="orbGlow" x1="0" y1="0" x2="1" y2="0.4">
          <stop offset="0" stop-color="#2A6CB4"/>
          <stop offset="1" stop-color="#6AA6BA"/>
        </linearGradient>
        <linearGradient id="waveTint" x1="0" y1="0" x2="1" y2="0">
          <stop offset="0" stop-color="#3478B8"/>
          <stop offset="1" stop-color="#4A8BC0"/>
        </linearGradient>
      </defs>
      <circle class="corner-orb" cx="808" cy="-155" r="330" fill="url(#orbGlow)"/>
      <path class="bottom-wave" d="M0 1035 C 70 1005, 150 990, 240 1000 C 330 1010, 380 985, 460 975 L 520 975 L 520 1200 L 0 1200 Z" fill="url(#waveTint)"/>
    </svg>

    <h1 class="headline">How to Launch<br>a Multi-Million<br>Business From<br>Scratch</h1>

    <p class="course-name">The Lantern Ledger Plan</p>

    <a class="cta-button" href="#">Sign Up Today!</a>

    <div class="hosts-photo" role="img" aria-label="Photo of the two course hosts standing side by side, cut out against the blue background"></div>
  </main>
</body>
</html>
```